3 Sympathy Cards for Veterinary Hospital

Hi. Meadowbrook Pet Hospital is a Veterinary Hospital in Australia. We need sympathy cards to send to grieving clients after the loss of their beloved pets.
I have attached the old designs, but we have rebranded and need something to suit our new image.

The cards should have a nice message and appeal to every owner.
They need to match our current branding, but the cards are for the clients, not to advertise us, so not too much branding.
The current cards are attached and they are good because they show a variety of animals so clients might identify with one of them.
I have attached a brown to green gradient that we use on some designs, you don't have to use it, but consider it.
I have attached a logo on background used in some of our new designs, consider using it.
I have attached a font that we use for most new branding.

Target Market(s)

Women 25 to 44

Industry/Entity Type

Veterinary

Font styles to use
Sans Serif
Script

Colors
fac994
cadf82

Requirements
Must have
• IMPORTANT - 3 different designs for the different types of pets.
• 1. Dog.
• 2. Cat.
• 3. Everything else (Rabbits, lizards, ferrets, chickens, birds, mice, rats, snakes)
Nice to have
• Caring and compassionate message.
Should not have
• Too much branding.

```html
<!DOCTYPE html>
<html lang="en">
<head>
<meta charset="utf-8">
<title>Sympathy Card – Cats</title>
<link rel="stylesheet" href="https://fonts.googleapis.com/css2?family=Alfa+Slab+One&family=Arimo:wght@400;700&display=swap">
<style>
  :root {
    --paper: #ffffff;
    --leaf-green: #c9de82;
    --title-white: #ffffff;
    --brand-brown: #4a2a16;
    --ink: #2b2b2b;
    --ginger: #e9a46a;
    --cat-grey: #8f8a84;
    --cat-brown: #a48a6e;
  }
  * { margin: 0; padding: 0; box-sizing: border-box; }
  html, body { width: 857px; height: 1200px; overflow: hidden; background: var(--paper); }
  .card {
    position: relative;
    width: 857px;
    height: 1200px;
    background: var(--paper);
    font-family: "Arimo", Arial, sans-serif;
  }

  /* Back panel (prints upside down for folding) */
  .card-back {
    position: absolute;
    left: 0; top: 0;
    width: 857px; height: 639px;
  }
  .imprint {
    position: absolute;
    left: 0; top: 114px;
    width: 857px;
    transform: rotate(180deg);
    text-align: center;
    color: var(--ink);
    font-size: 15px;
    line-height: 21px;
  }
  .imprint-illustration {
    position: absolute;
    left: 386px; top: 160px;
    width: 100px; height: 110px;
    border-radius: 40px;
    background: radial-gradient(ellipse at center, #f3cfa9 0%, #f7e3cf 60%, var(--paper) 100%);
  }

  /* Front panel */
  .card-front {
    position: absolute;
    left: 0; top: 639px;
    width: 857px; height: 561px;
    background: var(--leaf-green);
    overflow: hidden;
  }
  .brand-name {
    position: absolute;
    left: 29px; top: 92px;
    width: 160px;
    color: var(--brand-brown);
    font-family: "Arimo", Arial, sans-serif;
    font-weight: 700;
    font-size: 15px;
    line-height: 18px;
    text-transform: uppercase;
  }
  .card-title {
    position: absolute;
    left: 0; top: 218px;
    width: 857px;
    text-align: center;
    color: var(--title-white);
    font-family: "Alfa Slab One", "Rockwell", serif;
    font-weight: 400;
    font-size: 62px;
    line-height: 1;
    letter-spacing: 1px;
  }
  .cat-lineup {
    position: absolute;
    left: 26px; top: 300px;
    width: 805px; height: 261px;
    background: linear-gradient(90deg,
      var(--cat-brown) 0%, var(--ginger) 14%, var(--cat-grey) 26%,
      #e6ddd2 38%, var(--cat-brown) 50%, #b7b2ab 62%,
      #a9a39a 74%, #6f7280 88%, #8a8d99 100%);
    opacity: 0.85;
    border-radius: 48px 48px 0 0;
  }
</style>
</head>
<body>
  <main class="card">
    <section class="card-back">
      <div class="imprint-illustration" role="img" aria-label="Small line illustration of a ginger tabby cat lying on its back"></div>
      <p class="imprint">© Copyright 2017 Fernlea Card Co.<br>P.O Box 218, Glenvale 4350 | Ph 1800 4127 63</p>
    </section>

    <section class="card-front">
      <p class="brand-name">Meadowbrook<br>Pet Hospital</p>
      <h1 class="card-title">The Sympathy</h1>
      <div class="cat-lineup" role="img" aria-label="Photograph of eight cats of different breeds and colours sitting in a row"></div>
    </section>
  </main>
</body>
</html>
```